New Company Business Card design

Looking for a corporate looking business card utilising my new logo design - the logo i would like embossed as one option and flat as another - simplistic but stylish - less is more - we are an import export business launching into the market - i would like a couple of options as main background - Grey or Black

```html
<!DOCTYPE html>
<html lang="en">
<head>
<meta charset="utf-8">
<title>Meridian Trade Partners – Business Card</title>
<link href="https://fonts.googleapis.com/css2?family=Lato:wght@400;700;900&display=swap" rel="stylesheet">
<style>
  :root {
    --stage: #1c1c1e;
    --card-dark: #161617;
    --card-light: #ffffff;
    --brand-blue: #2a7bc8;
    --silver: #b9b9bc;
    --ink: #3a3a3c;
    --rule: #7d7d80;
  }
  html, body {
    margin: 0;
    width: 1200px;
    height: 1200px;
    overflow: hidden;
    background: var(--stage);
    font-family: "Lato", Arial, sans-serif;
  }
  .card {
    position: absolute;
    left: 150px;
    width: 900px;
    height: 514px;
    overflow: hidden;
    box-shadow: 0 14px 40px rgba(0,0,0,0.55);
  }
  .card--back { top: 70px; background: var(--card-dark); }
  .card--front { top: 616px; background: var(--card-light); }

  .brand {
    position: absolute;
    display: flex;
    align-items: center;
    gap: 18px;
    font-weight: 700;
    letter-spacing: 0.04em;
    text-transform: uppercase;
    white-space: nowrap;
  }
  .brand__dot {
    width: 30px;
    height: 30px;
    border-radius: 50%;
    flex: none;
  }
  .card--back .brand {
    left: 0; right: 0; top: 230px;
    justify-content: center;
    font-size: 38px;
    color: var(--silver);
  }
  .card--back .brand__dot { background: var(--silver); }

  .card--front .brand {
    right: 40px; top: 215px;
    font-size: 32px;
    color: var(--brand-blue);
  }
  .card--front .brand__dot { background: var(--brand-blue); }

  .holder {
    position: absolute;
    left: 0; top: 58px;
  }
  .holder__name {
    display: inline-block;
    margin: 0;
    padding: 6px 28px 6px 70px;
    background: var(--brand-blue);
    font-size: 38px;
    line-height: 44px;
    font-weight: 400;
    color: #fff;
    letter-spacing: 0.01em;
    white-space: nowrap;
  }
  .holder__first { font-weight: 900; }
  .holder__title {
    margin: 4px 0 0 70px;
    font-size: 23px;
    font-weight: 400;
    color: var(--brand-blue);
  }
  .divider {
    position: absolute;
    left: 150px; right: 40px; top: 316px;
    height: 2px;
    background: var(--rule);
  }
  .contact {
    position: absolute;
    left: 100px; top: 336px;
    margin: 0; padding: 0;
    list-style: none;
    font-size: 23px;
    color: var(--ink);
  }
  .contact li {
    display: flex;
    align-items: center;
    gap: 14px;
    height: 38px;
    white-space: nowrap;
  }
  .contact svg { width: 26px; height: 26px; flex: none; }
  .address {
    position: absolute;
    right: 40px; top: 355px;
    margin: 0;
    text-align: right;
    font-style: normal;
    font-size: 23px;
    line-height: 1.45;
    color: var(--ink);
    white-space: nowrap;
  }
</style>
</head>
<body>
  <section class="card card--back" aria-label="Card back">
    <div class="brand"><span class="brand__dot"></span>Meridian Trade Partners</div>
  </section>

  <section class="card card--front" aria-label="Card front">
    <div class="holder">
      <h1 class="holder__name"><span class="holder__first">MARTIN</span> HOLLOWAY</h1>
      <p class="holder__title">Managing Director</p>
    </div>

    <div class="brand"><span class="brand__dot"></span>Meridian Trade Partners</div>

    <div class="divider"></div>

    <ul class="contact">
      <li>
        <svg viewBox="0 0 26 26" aria-hidden="true"><circle cx="13" cy="13" r="13" fill="var(--brand-blue)"/><path d="M9 7l3 3-1.6 1.6a8 8 0 0 0 4 4L16 14l3 3-1.8 1.8C12 18.5 7.5 14 7.2 8.8z" fill="#fff"/></svg>
        555-014-2290
      </li>
      <li>
        <svg viewBox="0 0 26 26" aria-hidden="true"><circle cx="13" cy="13" r="13" fill="var(--brand-blue)"/><rect x="6.5" y="8.5" width="13" height="9" fill="#fff"/><path d="M6.5 8.5L13 13.5l6.5-5" fill="none" stroke="var(--brand-blue)" stroke-width="1.3"/></svg>
        info@meridiantradepartners.com
      </li>
      <li>
        <svg viewBox="0 0 26 26" aria-hidden="true"><circle cx="13" cy="13" r="13" fill="var(--brand-blue)"/><g fill="none" stroke="#fff" stroke-width="1.3"><circle cx="13" cy="13" r="6.5"/><ellipse cx="13" cy="13" rx="3" ry="6.5"/><path d="M6.5 13h13M7.5 9.8h11M7.5 16.2h11"/></g></svg>
        www.meridiantradepartners.com
      </li>
    </ul>

    <address class="address">418 Harbor View Road<br>Portside WA 98110</address>
  </section>
</body>
</html>
```